Business Card Design

we are Marrowbank Farms & we would like a business card that stands out from the crowd and that we can apply this design to our products as we will be also placing orders for labels and stickers in the future

Industry/Entity Type

Business

Contact Information for Business Card

Packing Shed : 53 617 904
mobile : 0412 583 091
email : marrowbankfarms@kestrelnet.com
address : Copperbark Lane Tarrowin 4571

```html
<!DOCTYPE html>
<html lang="en">
<head>
<meta charset="utf-8">
<title>Marrowbank Farms – Business Card</title>
<link rel="stylesheet" href="https://fonts.googleapis.com/css2?family=Baloo+2:wght@600&family=Open+Sans:wght@400;600&display=swap">
<style>
  :root {
    --backdrop: #b8a321;
    --backdrop-edge: #6e6418;
    --card-purple: #6a2168;
    --card-ink: #ffffff;
    --berry-red: #e0262b;
    --rule: #a77aa6;
  }
  * { margin: 0; padding: 0; box-sizing: border-box; }
  html, body {
    width: 1200px;
    height: 677px;
    overflow: hidden;
  }
  body {
    background: radial-gradient(ellipse at center, var(--backdrop) 0%, var(--backdrop-edge) 100%);
    position: relative;
    font-family: "Open Sans", Arial, sans-serif;
  }
  .card {
    position: absolute;
    top: 196px;
    width: 500px;
    height: 286px;
    background: var(--card-purple);
    color: var(--card-ink);
    box-shadow: 0 10px 24px rgba(0, 0, 0, 0.35);
  }
  .card--front { left: 70px; }
  .card--back { left: 630px; }

  .brand-name {
    font-family: "Baloo 2", "Trebuchet MS", sans-serif;
    font-weight: 600;
    color: var(--card-ink);
    line-height: 1;
  }

  .front-lockup {
    position: absolute;
    inset: 0;
    display: flex;
    flex-direction: column;
    align-items: center;
    justify-content: center;
    gap: 16px;
  }
  .front-lockup .brand-mark {
    width: 54px;
    height: 54px;
    border-radius: 50%;
    background: var(--berry-red);
  }
  .front-lockup .brand-name { font-size: 38px; }

  .back-header {
    position: absolute;
    left: 36px;
    top: 44px;
    display: flex;
    align-items: center;
    gap: 16px;
  }
  .back-header .brand-mark {
    width: 44px;
    height: 44px;
    border-radius: 50%;
    background: var(--card-ink);
  }
  .back-header .brand-name { font-size: 26px; }

  .divider {
    position: absolute;
    left: 28px;
    right: 0;
    top: 126px;
    height: 2px;
    background: var(--rule);
  }

  .contact-list {
    position: absolute;
    left: 40px;
    top: 168px;
    display: grid;
    grid-template-columns: 88px 20px auto;
    row-gap: 4px;
    font-size: 12.5px;
    line-height: 1.2;
  }
  .contact-label { font-weight: 600; }
</style>
</head>
<body>
  <section class="card card--front" aria-label="Business card front">
    <div class="front-lockup">
      <span class="brand-mark" aria-hidden="true"></span>
      <h1 class="brand-name">Marrowbank Farms</h1>
    </div>
  </section>

  <section class="card card--back" aria-label="Business card back">
    <div class="back-header">
      <span class="brand-mark" aria-hidden="true"></span>
      <h2 class="brand-name">Marrowbank Farms</h2>
    </div>
    <div class="divider"></div>
    <dl class="contact-list">
      <dt class="contact-label">Packing Shed</dt><span>:</span><dd>53 617 904</dd>
      <dt class="contact-label">Mobile</dt><span>:</span><dd>0412 583 091</dd>
      <dt class="contact-label">Email</dt><span>:</span><dd>marrowbankfarms@kestrelnet.com</dd>
      <dt class="contact-label">Address</dt><span>:</span><dd>Copperbark Lane Tarrowin 4571</dd>
    </dl>
  </section>
</body>
</html>
```